SKILLSTEP is a training facility that offers training or entry level positions in the oil and gas i

We are needing a business card design for a new business called SKILLSTEP Industry training Inc. We are a training facility offering courses for entry level positions in the oil and gas industry. We like to keep the design in the colours of our logo. we like this also on the card "Get Prepared For A Flexible Career You Can Build On"

Industry/Entity Type

Oil And Gas

Contact Information for Business Card

Dorian Wexley
RR3 Site 9 Comp27
Fort St. John, BC, V2K8P3
250.418.5069 cell
250.418.7312 office
dorian@SKILLSTEPNORTH.ca
WWW.SKILLSTEPNORTH.CA

```html
<!DOCTYPE html>
<html lang="en">
<head>
<meta charset="utf-8">
<title>SKILLSTEP Industry Training Inc. – Business Card</title>
<link rel="stylesheet" href="https://fonts.googleapis.com/css2?family=Arimo:wght@400;700&display=swap">
<style>
  :root {
    --backdrop: #e7e3dc;
    --card-white: #ffffff;
    --brand-orange: #f26a24;
    --brand-grey: #55575a;
    --ink: #151515;
    --shadow: rgba(0, 0, 0, 0.18);
  }
  * { box-sizing: border-box; margin: 0; padding: 0; }
  html, body {
    width: 1200px;
    height: 800px;
    overflow: hidden;
    background: var(--backdrop);
    font-family: "Arimo", Arial, sans-serif;
  }
  .stage {
    position: relative;
    width: 1200px;
    height: 800px;
  }
  .card {
    position: absolute;
    width: 540px;
    height: 309px;
    background: var(--card-white);
    box-shadow: 0 6px 18px var(--shadow);
    overflow: hidden;
  }
  .card--front { left: 40px; top: 140px; }
  .card--back  { left: 620px; top: 350px; }

  .brand {
    display: flex;
    align-items: center;
    gap: 12px;
    color: var(--brand-grey);
    font-weight: 700;
    white-space: nowrap;
  }
  .brand__dot {
    flex: none;
    border-radius: 50%;
    background: var(--brand-grey);
  }
  .brand__name { letter-spacing: 0.02em; }

  .card--front .brand {
    position: absolute;
    left: 50%;
    top: 50%;
    transform: translate(-50%, -50%);
    font-size: 26px;
  }
  .card--front .brand__dot { width: 38px; height: 38px; }

  .back__top {
    height: 112px;
    display: flex;
    align-items: center;
    justify-content: center;
  }
  .card--back .brand { font-size: 19px; gap: 10px; }
  .card--back .brand__dot { width: 28px; height: 28px; }

  .back__band {
    position: absolute;
    left: 0; right: 0; bottom: 0;
    top: 112px;
    background: var(--brand-orange);
    color: var(--ink);
    display: flex;
    flex-direction: column;
    align-items: center;
    justify-content: center;
    text-align: center;
    font-size: 15px;
    line-height: 1.3;
  }
  .contact__gap { height: 8px; }
</style>
</head>
<body>
  <main class="stage">
    <section class="card card--front" aria-label="Card front">
      <div class="brand">
        <span class="brand__dot"></span>
        <span class="brand__name">SKILLSTEP Industry Training Inc.</span>
      </div>
    </section>

    <section class="card card--back" aria-label="Card back">
      <div class="back__top">
        <div class="brand">
          <span class="brand__dot"></span>
          <span class="brand__name">SKILLSTEP Industry Training Inc.</span>
        </div>
      </div>
      <address class="back__band" style="font-style:normal">
        <span class="contact__line">Dorian Wexley RR3 Site 9 Comp27 Fort St.</span>
        <span class="contact__line">John, BC, V2K8P3</span>
        <span class="contact__line">250.418.5069</span>
        <span class="contact__line">250.418.7312</span>
        <span class="contact__gap"></span>
        <span class="contact__line">dorian@SKILLSTEPNORTH.ca</span>
        <span class="contact__line">WWW.SKILLSTEPNORTH.CA</span>
      </address>
    </section>
  </main>
</body>
</html>
```